Business Card for Consulting Company

I would need a business card for my consulting company - the company brand and logos are defined and shared as part of this project. The proposed design for the business card can be reused as inspiration for my email signature.

```html
<!DOCTYPE html>
<html lang="en">
<head>
<meta charset="utf-8">
<title>Corvano – Business Card</title>
<link href="https://fonts.googleapis.com/css2?family=Arimo:wght@400;700&display=swap" rel="stylesheet">
<style>
  :root {
    --backdrop-light: #ecebe8;
    --backdrop-dark: #d6d5d1;
    --card: #2d2e30;
    --card-pattern-light: #3a3b3e;
    --card-pattern-dark: #262729;
    --teal: #17aeb0;
    --white: #ffffff;
    --muted: #e6e6e6;
  }
  html, body {
    margin: 0;
    width: 1200px;
    height: 801px;
    overflow: hidden;
  }
  body {
    background: radial-gradient(ellipse at 40% 30%, var(--backdrop-light), var(--backdrop-dark));
    font-family: "Arimo", Arial, sans-serif;
    position: relative;
  }
  .card {
    position: absolute;
    top: 250px;
    width: 510px;
    height: 300px;
    background: var(--card);
    border-bottom: 4px solid var(--teal);
    border-left: 4px solid var(--teal);
    box-shadow: 0 14px 30px rgba(0,0,0,0.25);
    overflow: hidden;
  }
  .card--front { left: 60px; }
  .card--back { left: 626px; }

  .front__tab {
    position: absolute;
    top: 0;
    right: 28px;
    width: 14px;
    height: 26px;
    background: var(--teal);
  }
  .front__person {
    position: absolute;
    top: 34px;
    right: 28px;
    text-align: right;
  }
  .person__name {
    margin: 0;
    color: var(--teal);
    font-weight: 700;
    font-size: 21px;
  }
  .person__role {
    margin: 4px 0 0;
    color: var(--muted);
    font-size: 14px;
  }
  .brand {
    position: absolute;
    left: 34px;
    top: 130px;
    display: flex;
    align-items: center;
    gap: 10px;
  }
  .brand__dot {
    width: 18px;
    height: 18px;
    border-radius: 50%;
    background: var(--teal);
  }
  .brand__name {
    color: var(--teal);
    font-weight: 700;
    font-size: 34px;
    letter-spacing: 0.5px;
  }
  .contact {
    position: absolute;
    left: 34px;
    bottom: 26px;
    margin: 0;
    padding: 0;
    list-style: none;
  }
  .contact__item {
    display: flex;
    align-items: center;
    gap: 10px;
    color: var(--white);
    font-size: 14px;
    line-height: 24px;
  }
  .contact__icon {
    width: 13px;
    height: 13px;
    fill: var(--teal);
    flex: none;
  }

  .back__pattern {
    position: absolute;
    inset: 0;
    background: linear-gradient(135deg, var(--card-pattern-dark) 0%, var(--card) 45%, var(--card-pattern-light) 100%);
  }
  .back__brand {
    position: absolute;
    right: 40px;
    top: 180px;
    display: flex;
    align-items: center;
    gap: 10px;
  }
  .back__brand .brand__name { font-size: 26px; }
  .back__brand .brand__dot { width: 14px; height: 14px; }
</style>
</head>
<body>

<section class="card card--front" aria-label="Card front">
  <div class="front__tab"></div>
  <div class="front__person">
    <p class="person__name">Maren Holt</p>
    <p class="person__role">Founder &amp; CEO</p>
  </div>

  <div class="brand">
    <span class="brand__dot"></span>
    <span class="brand__name">Corvano</span>
  </div>

  <ul class="contact">
    <li class="contact__item">
      <svg class="contact__icon" viewBox="0 0 24 24" aria-hidden="true"><path d="M6.6 10.8a15.1 15.1 0 0 0 6.6 6.6l2.2-2.2a1 1 0 0 1 1-.25 11.4 11.4 0 0 0 3.6.57 1 1 0 0 1 1 1V20a1 1 0 0 1-1 1A17 17 0 0 1 3 4a1 1 0 0 1 1-1h3.5a1 1 0 0 1 1 1c0 1.25.2 2.45.57 3.57a1 1 0 0 1-.25 1z"/></svg>
      +41 79 000 12 34
    </li>
    <li class="contact__item">
      <svg class="contact__icon" viewBox="0 0 24 24" aria-hidden="true"><path d="M2 5h20v14H2z M4 7v.5l8 5 8-5V7l-8 5z" fill-rule="evenodd"/></svg>
      maren.h@corvano.ch
    </li>
    <li class="contact__item">
      <svg class="contact__icon" viewBox="0 0 24 24" aria-hidden="true"><circle cx="12" cy="12" r="10"/></svg>
      www.corvano.ch
    </li>
  </ul>
</section>

<section class="card card--back" aria-label="Card back">
  <div class="back__pattern" role="img" aria-label="Embossed repeating brand pattern in dark grey tones"></div>
  <div class="back__brand">
    <span class="brand__dot"></span>
    <span class="brand__name">Corvano</span>
  </div>
</section>

</body>
</html>
```